Business Card Design & logo

Residential building renovation and maintenance work.
All carpentry and joinery needs.
Laying solid timber and floating floors.
Kitchen and bathroom makeovers and modifications.
Interior fitouts,
small job specialist. tiling, plastering, painting,

I would like a silver background. With the use of different shades of grey, rustic orange, black and white.
I do not want pictures of hammers, chisels etc. I am looking for a logo to be incorporated into the card.

Carpentry

Contact Information for Business Card

BTQ Renovations and Maintenance
Lewis Tolbane
0471852036
info@btqfixes.com.au
btqfixes.com.au

```html
<!DOCTYPE html>
<html lang="en">
<head>
<meta charset="utf-8">
<title>BTQ Renovations and Maintenance – Business Card</title>
<link href="https://fonts.googleapis.com/css2?family=Oswald:wght@400;500&display=swap" rel="stylesheet">
<style>
  :root {
    --page: #e4e4e4;
    --silver: #d9d8d8;
    --charcoal: #4a4a4a;
    --card-black: #2a2a2a;
    --rust: #cf5424;
    --white: #ffffff;
  }
  * { box-sizing: border-box; margin: 0; padding: 0; }
  html, body {
    width: 1200px; height: 1200px; overflow: hidden;
    background: var(--page);
    font-family: "Oswald", "Arial Narrow", sans-serif;
  }
  .canvas { position: relative; width: 1200px; height: 1200px; }

  .card {
    position: absolute; width: 680px; height: 389px;
    box-shadow: 0 6px 18px rgba(0,0,0,0.18);
    overflow: hidden;
  }

  /* Shared brand name: plain company name in the body text style */
  .brand-name {
    font-weight: 400; white-space: nowrap; letter-spacing: 0.8px; line-height: 1;
  }
  .brand-square { background: var(--rust); flex: none; }

  /* Front */
  .card-front { left: 260px; top: 90px; background: var(--silver); }
  .brand {
    position: absolute; left: 36px; top: 180px;
    display: flex; align-items: center; gap: 10px;
  }
  .brand .brand-square { width: 14px; height: 14px; }
  .brand .brand-name { color: var(--charcoal); font-size: 21px; }
  .divider {
    position: absolute; left: 392px; top: 125px; width: 3px; height: 160px;
    background: var(--rust);
  }
  .contact { position: absolute; left: 418px; top: 135px; }
  .person-name {
    color: var(--charcoal); font-weight: 500; font-size: 32px;
    letter-spacing: 1px; margin-bottom: 14px;
  }
  .contact-line {
    display: flex; align-items: center; gap: 12px;
    color: var(--charcoal); font-size: 18px; letter-spacing: 0.8px;
    margin-bottom: 8px;
  }
  .contact-line svg { width: 15px; height: 15px; flex: none; }
  .front-band {
    position: absolute; left: 0; bottom: 0; width: 380px; height: 26px;
    background: var(--rust);
  }

  /* Back */
  .card-back { left: 260px; top: 560px; background: var(--card-black); }
  .services {
    position: absolute; left: 60px; top: 45px; list-style: none;
    color: var(--white); font-size: 21px; letter-spacing: 1px; line-height: 1.5;
  }
  .back-brand {
    position: absolute; right: 40px; bottom: 40px;
    display: flex; align-items: center; gap: 10px;
  }
  .back-brand .brand-square { width: 12px; height: 12px; }
  .back-brand .brand-name { color: var(--white); font-size: 18px; }

  /* Standalone name block */
  .logo-lockup {
    position: absolute; right: 30px; bottom: 50px;
    display: flex; align-items: center; gap: 12px;
  }
  .logo-lockup .brand-square { width: 18px; height: 18px; }
  .logo-lockup .brand-name { color: var(--charcoal); font-size: 28px; }
</style>
</head>
<body>
<main class="canvas">

  <section class="card card-front" aria-label="Business card front">
    <div class="brand">
      <span class="brand-square"></span>
      <span class="brand-name">BTQ Renovations and Maintenance</span>
    </div>
    <div class="divider"></div>
    <div class="contact">
      <p class="person-name">Lewis Tolbane</p>
      <p class="contact-line">
        <svg viewBox="0 0 16 16" aria-hidden="true"><path fill="#cf5424" d="M2 6c0-2 3-3 6-3s6 1 6 3v1h-3V5.8C10 5.3 9 5 8 5s-2 .3-3 .8V7H2zM4 8h8l1 5H3z"/></svg>
        <span>0471852036</span>
      </p>
      <p class="contact-line">
        <svg viewBox="0 0 16 16" aria-hidden="true"><rect x="1" y="3" width="14" height="10" fill="#cf5424"/><path d="M1 3l7 6 7-6" fill="none" stroke="#d9d8d8" stroke-width="1.3"/></svg>
        <span>info@btqfixes.com.au</span>
      </p>
      <p class="contact-line">
        <svg viewBox="0 0 16 16" aria-hidden="true"><g fill="none" stroke="#cf5424" stroke-width="1.2"><circle cx="8" cy="8" r="6.2"/><ellipse cx="8" cy="8" rx="2.6" ry="6.2"/><path d="M2 8h12"/></g></svg>
        <span>btqfixes.com.au</span>
      </p>
    </div>
    <div class="front-band"></div>
  </section>

  <section class="card card-back" aria-label="Business card back">
    <ul class="services">
      <li>- All carpentry and joinery</li>
      <li>- Laying solid timber and floating floors</li>
      <li>- Kitchen makeovers and modifications</li>
      <li>- Bathroom makeovers and modifications</li>
      <li>- Interior fitouts</li>
      <li>- Tiling</li>
      <li>- Plastering</li>
      <li>- Painting</li>
    </ul>
    <div class="back-brand">
      <span class="brand-square"></span>
      <span class="brand-name">BTQ Renovations and Maintenance</span>
    </div>
  </section>

  <div class="logo-lockup">
    <span class="brand-square"></span>
    <span class="brand-name">BTQ Renovations and Maintenance</span>
  </div>

</main>
</body>
</html>
```